Dark Comedy Movie Poster

We need a poster design for our short film BRAM that we just wrapped on.
It's a dark comedy
Bram explores the world of loneliness through the lens of a manic man-child. Bram wants nothing more than the approval of others, giving every last bit of energy to the cause. But his ravenous attempts accomplish the opposite, turning others off. His desperation is authentic, his lonliness cavernous.
Here is a link to the film
https://clipvault.example/548207316
Password: Bram42
I want you, the artist, to pitch me an idea in any way you want. I'm open to absolutely anything right now. Once I have some pitches from you all my production team and I will sort through them and pick the best fit!
-Owen

```html
<!DOCTYPE html>
<html lang="en">
<head>
<meta charset="utf-8">
<title>BRAM – A Short Film by Owen Marlow</title>
<link rel="stylesheet" href="https://fonts.googleapis.com/css2?family=Amatic+SC:wght@400;700&display=swap">
<style>
  :root {
    --poster-red: #d9110f;
    --poster-red-deep: #a5060a;
    --poster-red-light: #ee2a22;
    --title-cream: #f2e3a6;
  }
  html, body {
    margin: 0;
    padding: 0;
    width: 923px;
    height: 1200px;
    overflow: hidden;
    background: var(--poster-red);
  }
  .poster {
    position: relative;
    width: 923px;
    height: 1200px;
    overflow: hidden;
  }
  .poster__backdrop {
    position: absolute;
    inset: 0;
    background:
      radial-gradient(ellipse at 50% 45%, var(--poster-red-light) 0%, var(--poster-red) 55%, var(--poster-red-deep) 100%);
  }
  .poster__credit {
    position: absolute;
    top: 92px;
    left: 0;
    right: 0;
    margin: 0;
    text-align: center;
    font-family: "Amatic SC", sans-serif;
    font-weight: 700;
    font-size: 38px;
    letter-spacing: 2px;
    color: var(--title-cream);
  }
  .poster__title {
    position: absolute;
    top: 400px;
    left: 0;
    right: 0;
    margin: 0;
    text-align: center;
    font-family: "Amatic SC", sans-serif;
    font-weight: 400;
    font-size: 400px;
    line-height: 1;
    letter-spacing: 18px;
    color: var(--title-cream);
  }
</style>
</head>
<body>
  <main class="poster">
    <div class="poster__backdrop" role="img" aria-label="Close-up photograph of a heap of glossy red candy pieces filling the whole poster"></div>
    <p class="poster__credit">A short film by Owen Marlow</p>
    <h1 class="poster__title">BRAM</h1>
  </main>
</body>
</html>
```